Business Card cabinets and cabinets components making company.

the card should be formal and interesting at the same time. The main colors will be black and white.

Font styles to use
Sans Serif

Colors

Designer to choose only greyscale colors for use in the design.

Requirements
Must have
• At least must have the followings:
office phone
cell phone
address
position
name
email
web

```html
<!DOCTYPE html>
<html lang="en">
<head>
<meta charset="utf-8">
<title>Boxwell Business Card</title>
<link rel="stylesheet" href="https://fonts.googleapis.com/css2?family=Roboto:wght@300;400;500&display=swap">
<style>
  :root {
    --backdrop: #9b9b9b;
    --card-white: #ffffff;
    --ink: #1c1d1f;
    --ink-soft: #2a2a2a;
    --rule: #3a3a3a;
    --art-light: #e4e4e4;
    --art-mid: #7d7e80;
  }
  * { margin: 0; padding: 0; box-sizing: border-box; }
  html, body {
    width: 1200px;
    height: 900px;
    overflow: hidden;
    background: var(--backdrop);
    font-family: "Roboto", Arial, sans-serif;
    color: var(--ink);
  }
  .canvas { position: relative; width: 1200px; height: 900px; }
  .card {
    position: absolute;
    top: 214px;
    width: 271px;
    height: 474px;
    border-radius: 24px;
    overflow: hidden;
  }
  .card-back { left: 288px; background: var(--ink); }
  .card-back .artwork {
    width: 100%;
    height: 100%;
    background: linear-gradient(155deg,
      var(--art-light) 0%,
      var(--art-mid) 30%,
      var(--ink) 58%,
      var(--ink) 78%,
      var(--art-mid) 100%);
  }
  .card-front { left: 641px; background: var(--card-white); text-align: center; }
  .brand {
    position: absolute;
    top: 290px;
    top: 76px;
    left: 0;
    width: 100%;
    font-size: 38px;
    font-weight: 500;
    letter-spacing: -0.5px;
    color: var(--ink);
  }
  .person-name {
    position: absolute;
    top: 236px;
    width: 100%;
    font-size: 19px;
    font-weight: 500;
  }
  .person-role {
    position: absolute;
    top: 260px;
    width: 100%;
    font-size: 14px;
    font-weight: 300;
    color: var(--ink-soft);
  }
  .icon-row {
    position: absolute;
    top: 284px;
    left: 48px;
    width: 174px;
    height: 18px;
  }
  .contact-list {
    position: absolute;
    top: 311px;
    width: 100%;
    list-style: none;
    font-size: 13.5px;
    font-weight: 300;
    line-height: 19px;
  }
  .divider {
    position: absolute;
    top: 396px;
    left: 48px;
    width: 174px;
    height: 1px;
    background: var(--rule);
  }
  .address {
    position: absolute;
    top: 406px;
    width: 100%;
    font-size: 13.5px;
    font-weight: 300;
    line-height: 16px;
    font-style: normal;
  }
</style>
</head>
<body>
<main class="canvas">
  <section class="card card-back">
    <div class="artwork" role="img" aria-label="Large black and white cabinet brand graphic filling the card back"></div>
  </section>

  <section class="card card-front">
    <div class="brand">Boxwell</div>
    <h1 class="person-name">Daniel Mercer</h1>
    <p class="person-role">Manager</p>

    <svg class="icon-row" viewBox="0 0 174 18" aria-hidden="true">
      <line x1="0" y1="9" x2="50" y2="9" stroke="#3a3a3a" stroke-width="1"/>
      <line x1="124" y1="9" x2="174" y2="9" stroke="#3a3a3a" stroke-width="1"/>
      <circle cx="59" cy="9" r="8" fill="#1c1d1f"/>
      <path d="M54.5 8 q4.5 -3 9 0 v1.5 h-2 v-1 q-2.5 -1 -5 0 v1 h-2z M56 10 h6 l1 3 h-8z" fill="#fff"/>
      <circle cx="78" cy="9" r="8" fill="#1c1d1f"/>
      <rect x="75" y="4" width="6" height="10" rx="1" fill="#fff"/>
      <rect x="76" y="5.5" width="4" height="6" fill="#1c1d1f"/>
      <circle cx="97" cy="9" r="8" fill="#1c1d1f"/>
      <rect x="92.5" y="5.5" width="9" height="7" fill="#fff"/>
      <path d="M92.5 5.5 L97 9.5 L101.5 5.5" fill="none" stroke="#1c1d1f" stroke-width="1"/>
      <circle cx="116" cy="9" r="8" fill="#1c1d1f"/>
      <circle cx="116" cy="9" r="5" fill="none" stroke="#fff" stroke-width="1.2"/>
      <ellipse cx="116" cy="9" rx="2" ry="5" fill="none" stroke="#fff" stroke-width="1"/>
      <line x1="111" y1="9" x2="121" y2="9" stroke="#fff" stroke-width="1"/>
    </svg>

    <ul class="contact-list">
      <li>123-456-2100</li>
      <li>123-456-2100</li>
      <li>hello@boxwellmail.com</li>
      <li>www.boxwellcabinets.com</li>
    </ul>

    <div class="divider"></div>

    <address class="address">Your address, city<br>state, ZIP 0000</address>
  </section>
</main>
</body>
</html>
```